Diagram, Brochure and Flyer Design

Veltrion Systems is a cyber security software company that develops, implements and supports cyber security and information management end-point solutions that solve critical security and compliance issues when organisations transmit private or business sensitive information.

We do this by interfacing directly with an organisation’s existing information management systems and line of business applications to provide a ‘bridge’ to essential security systems and platforms for data that is transmitted via email, FTP, ‘Bring Your Own Devices’ (‘BYOD’) such as smart phones, iPads, etc, or during collaboration with third party organisations that use different systems and applications, and the Cloud.

Veltrion Systems, flagship product "Lumora" enables simple deployment by organisations with minimal change management to secure an organisation’s vulnerable digital assets.

Most importantly, Lumora enables organisations to secure data without replacing or losing functionality from existing systems (i.e. for compliance, collaboration or audit purposes, etc.).

We are seeking to design a series of corporate brochures, diagrams and flyers for an information security company as described above.

www.veltrion.com.au

Target Market(s)

Government and Corporates

Font styles to use
Sans Serif

Requirements
Must have
• Clean and professional
Nice to have
• Consistent look and feel
Should not have
• Too much wording (text)

```html
<!DOCTYPE html>
<html lang="en">
<head>
<meta charset="utf-8">
<title>Veltrion Systems – Lumora Flyer</title>
<link rel="stylesheet" href="https://fonts.googleapis.com/css2?family=Oswald:wght@300;500&family=Lato:wght@400;700&display=swap">
<style>
  :root {
    --stage: #b9b9b9;
    --paper: #ffffff;
    --ink: #1c1c1c;
    --grey: #6f6f6f;
    --soft: #e7e7e7;
    --orange: #e8700f;
    --black: #111111;
  }
  * { box-sizing: border-box; margin: 0; padding: 0; }
  html, body { width: 1200px; height: 790px; overflow: hidden; }
  body {
    background: var(--stage);
    font-family: "Lato", Arial, sans-serif;
    color: var(--ink);
    position: relative;
  }
  .panel {
    position: absolute;
    width: 570px;
    height: 392px;
    background: var(--paper);
    overflow: hidden;
    box-shadow: 0 6px 18px rgba(0,0,0,0.25);
  }
  .panel--front { left: 20px; top: 199px; }
  .panel--back { left: 610px; top: 199px; }
  .panel svg.shapes { position: absolute; inset: 0; }

  .brand {
    position: absolute;
    display: flex;
    align-items: center;
    gap: 8px;
    font-family: "Lato", Arial, sans-serif;
    font-weight: 700;
    color: var(--ink);
  }
  .brand__square { width: 14px; height: 14px; background: var(--ink); }
  .brand--front { left: 36px; top: 180px; font-size: 17px; }
  .brand--back { left: 0; right: 0; top: 70px; justify-content: center; font-size: 14px; }

  .headline {
    position: absolute;
    right: 20px;
    top: 284px;
    text-align: right;
    font-family: "Oswald", Arial, sans-serif;
    white-space: nowrap;
  }
  .headline__title { font-weight: 500; font-size: 30px; line-height: 1.1; color: var(--black); }
  .headline__tagline { font-weight: 300; font-size: 17px; line-height: 1.3; color: var(--grey); }

  .contact {
    position: absolute;
    left: 0; right: 0; top: 128px;
    text-align: center;
  }
  .contact__title {
    display: inline-block;
    font-family: "Lato", Arial, sans-serif;
    font-weight: 700;
    font-size: 17px;
    color: var(--orange);
    padding: 0 10px 4px;
    border-bottom: 1px solid var(--ink);
  }
  .contact__address { font-size: 9px; margin-top: 8px; color: var(--grey); }
  .contact__phone { font-size: 15px; margin-top: 4px; }
  .contact__email { font-size: 9px; margin-top: 4px; color: var(--grey); }
  .contact__web { font-size: 9px; font-weight: 700; letter-spacing: 2.5px; margin-top: 7px; }
</style>
</head>
<body>

<section class="panel panel--front">
  <svg class="shapes" width="570" height="392" viewBox="0 0 570 392">
    <defs>
      <linearGradient id="photoFade" x1="0" y1="0" x2="1" y2="0">
        <stop offset="0" stop-color="#ffffff"/>
        <stop offset="0.35" stop-color="#9a9a9a"/>
        <stop offset="1" stop-color="#3a3a3a"/>
      </linearGradient>
    </defs>
    <polygon class="photo" role="img" aria-label="Photo of a businessman in a suit touching a glowing cloud icon surrounded by device and email icons"
      points="220,0 570,0 570,238 305,254 262,284 240,200" fill="url(#photoFade)"/>
    <polygon class="corner-band corner-band--orange" points="0,150 60,130 60,152 0,172" fill="var(--orange)"/>
    <polygon class="corner-band corner-band--black" points="52,132 70,126 62,160 48,164" fill="var(--black)"/>
    <polygon class="band band--orange" points="40,392 96,392 300,252 272,254" fill="var(--orange)"/>
    <polygon class="band band--black" points="96,392 150,392 320,266 570,250 570,238 305,254" fill="var(--black)"/>
    <polygon class="band band--soft" points="320,266 570,250 570,262 340,276" fill="var(--soft)"/>
  </svg>

  <div class="brand brand--front"><span class="brand__square"></span>Veltrion Systems</div>

  <div class="headline">
    <div class="headline__title">Lumora&nbsp; for business</div>
    <div class="headline__tagline">Next generation&nbsp; data sharing platform</div>
  </div>
</section>

<section class="panel panel--back">
  <svg class="shapes" width="570" height="392" viewBox="0 0 570 392">
    <defs>
      <radialGradient id="softGlow" cx="0.75" cy="0.35" r="0.7">
        <stop offset="0" stop-color="#f7f7f7"/>
        <stop offset="1" stop-color="#ffffff"/>
      </radialGradient>
    </defs>
    <rect width="570" height="392" fill="url(#softGlow)"/>
    <path class="swoosh" d="M250,0 C420,60 500,170 570,300" fill="none" stroke="#ececec" stroke-width="22"/>
    <path class="swoosh" d="M300,0 C450,70 520,160 570,230" fill="none" stroke="#f1f1f1" stroke-width="14"/>
    <polygon class="band band--black" points="30,392 70,392 150,330 570,318 570,310 140,322" fill="var(--black)"/>
    <polygon class="band band--orange" points="140,322 570,310 570,290 470,292 440,300 160,306" fill="var(--orange)"/>
  </svg>

  <div class="brand brand--back"><span class="brand__square"></span>Veltrion Systems</div>

  <div class="contact">
    <div class="contact__title">CONTACT US:</div>
    <p class="contact__address">12 Harbour Lane, Riverton 3150 Australia</p>
    <p class="contact__phone">CALL US: +61 400 123 456</p>
    <p class="contact__email">info@veltrion.com.au</p>
    <p class="contact__web">www.veltrion.com.au</p>
  </div>
</section>

</body>
</html>
```